Redesign cement bags for leading cement producer in south east asia

We are from Larkfield cement and would like to redesign our bag to relaunch the product line. Our bags are made of high quality PP woven sack. We are one of the leading cement producers and we want our bags to have a Larkfield classy look on each visible side when it is loading in a truck or stacking on a pallet.

Thank you for interesting in this project. Good luck.

Project Deadline Extended Reason: Hi all, I have received requests to extend the deadline. Some of the work requires revising and some of them are still on process. To be fair, I also raise my budget to compensate the time. Thanks all for your participation. Added Sunday, July 10, 2016

Target Market(s)

Construction

Industry/Entity Type

Cement

Requirements
Must have
• You will have to design two bags for two cement grades. 52.5 is of higher grade and 42.5 is of lower grade. Both are similar in design but a distinctive colours to differentiate the two at once. Please look at Reference picture 2 for ideas.
Nice to have
• You do not have to change the original logo but the Larkfield cement word font changes are required. There are no restrictions to colours and font but please refrain from using feminine colours. Instructions on rear side of the bags are now included in the scope. Please create new layout and design new user friendly symbols.
Should not have
• Since cement is a dusty product, you need avoid some colours like black as background. The dust need to be less obvious to attract attention. Our previous base colour are shown in below.
• We want a fresh look on our bag, please do not just copy our old design and make small changes. I have attached our competitors' design, please refrain from using their design as well.
• It is recommend to do some research on cement bag sector.

```html
<!DOCTYPE html>
<html lang="en">
<head>
<meta charset="utf-8">
<title>Larkfield Cement – Bag Designs 52.5 &amp; 42.5</title>
<link href="https://fonts.googleapis.com/css2?family=Alfa+Slab+One&family=Roboto+Condensed:wght@300;400;700&display=swap" rel="stylesheet">
<style>
  :root{
    --bg:#e6e7e9;
    --white:#ffffff;
    --sun:#e8d21c;
    --sun-soft:#f6ee9c;
    --red:#e4194a;
    --blue:#21309a;
    --green:#1f9a4a;
    --ink:#2a2a2a;
  }
  *{box-sizing:border-box;margin:0;padding:0}
  html,body{width:1200px;height:1200px;overflow:hidden;background:var(--bg)}
  body{position:relative;font-family:"Roboto Condensed",Arial,sans-serif}

  .bag{position:absolute;display:flex;height:570px}
  .bag--premium{--grade:var(--red)}
  .bag--standard{--grade:var(--blue)}
  .bag--premium.bag--rear{left:200px;top:90px}
  .bag--premium.bag--face{left:56px;top:220px}
  .bag--standard.bag--rear{left:776px;top:350px}
  .bag--standard.bag--face{left:632px;top:480px}

  .bag__front{position:relative;width:312px;height:100%;background:var(--white);overflow:hidden}

  /* face panel */
  .bag__rays{position:absolute;left:0;top:0;width:100%;height:232px;
    background:radial-gradient(circle at 100% 100%,var(--white) 0%,var(--sun-soft) 35%,var(--sun) 100%)}
  .brand-box{position:absolute;left:20px;top:26px;width:100px;height:144px;background:var(--grade);
    border:3px solid var(--white);outline:2px solid var(--grade);display:flex;align-items:flex-end;justify-content:center;padding-bottom:16px}
  .brand-box__name{font-family:"Alfa Slab One",serif;color:var(--sun);font-size:11px;letter-spacing:.2px;white-space:nowrap}
  .product-band{position:absolute;left:0;top:232px;width:100%;height:88px;background:var(--grade);
    display:flex;align-items:center;justify-content:center}
  .product-band__word{font-family:"Alfa Slab One",serif;color:var(--sun);font-size:52px;letter-spacing:1px;line-height:1}
  .origin-tag{position:absolute;left:40px;top:326px;background:var(--green);color:var(--white);
    font-size:12px;font-weight:300;padding:2px 6px;text-transform:uppercase;white-space:nowrap}
  .origin-tag b{font-weight:700}
  .grade-mark{position:absolute;left:20px;top:470px;color:var(--grade);font-weight:700;line-height:.95;text-transform:uppercase}
  .grade-mark small{display:block;font-size:7px}
  .grade-mark strong{display:block;font-size:14px}
  .spec{position:absolute;left:20px;top:518px;font-size:8px;color:var(--ink);line-height:1.5}
  .usage-icons{position:absolute;right:18px;top:518px;display:flex;gap:5px}
  .usage-icon{width:28px;height:28px;border-radius:50%;background:var(--grade);border:2px solid var(--white);outline:1px solid var(--grade);
    color:var(--white);font-size:5px;font-weight:700;display:flex;align-items:center;justify-content:center;text-align:center;line-height:1}
  .usage-icon--weight{font-size:8px}

  /* rear panel */
  .rear__title{position:absolute;left:30px;top:106px;color:var(--grade);font-size:13px;font-weight:300}
  .rear__lead{position:absolute;left:30px;top:124px;color:var(--grade);font-size:8px;font-weight:300}
  .rear__brand{position:absolute;left:192px;top:28px;width:80px;height:104px;background:var(--grade);
    border:3px solid var(--white);outline:2px solid var(--grade);display:flex;align-items:flex-end;justify-content:center;padding-bottom:12px}
  .rear__brand span{font-family:"Alfa Slab One",serif;color:var(--sun);font-size:9px;white-space:nowrap}
  .mix-table{position:absolute;left:60px;top:152px;width:212px;border-collapse:collapse;color:var(--grade);font-size:9px}
  .mix-table th,.mix-table td{border:1px solid var(--grade);height:28px;text-align:center;font-weight:400}
  .mix-table th{height:20px}
  .cup{display:inline-block;width:8px;height:9px;border:1px solid var(--grade);border-top:none;border-radius:0 0 2px 2px}
  .note{position:absolute;left:60px;width:212px;border:1px solid var(--grade);border-radius:6px;color:var(--grade);
    font-size:8px;padding:8px 10px 0 150px;line-height:1.4}
  .note--store{top:262px;height:72px}
  .note--use{top:362px;height:110px;padding-top:74px}
  .rear__grade{position:absolute;left:212px;top:526px;color:var(--grade);font-weight:700;line-height:.9;text-transform:uppercase}
  .rear__grade span{display:block;font-size:15px}
  .rear__grade strong{display:block;font-size:26px}

  /* side gusset */
  .bag__side{position:relative;width:60px;height:100%;background:var(--grade);overflow:hidden}
  .side__icons{position:absolute;left:6px;top:14px;display:flex;gap:4px}
  .side__dot{width:22px;height:22px;border-radius:50%;background:var(--white)}
  .side__grade{position:absolute;left:4px;top:200px;width:140px;transform-origin:0 0;transform:rotate(-90deg);
    color:var(--white);font-weight:700;line-height:.92;text-transform:uppercase}
  .side__grade span{display:block;font-size:12px}
  .side__grade strong{display:block;font-size:22px}
  .side__word{position:absolute;left:4px;top:470px;width:240px;height:42px;transform-origin:0 0;transform:rotate(-90deg);
    font-family:"Alfa Slab One",serif;color:var(--sun);font-size:38px;line-height:42px;white-space:nowrap}
  .side__origin{position:absolute;left:47px;top:470px;width:240px;height:11px;transform-origin:0 0;transform:rotate(-90deg);
    background:var(--green);color:var(--white);font-size:7px;font-weight:300;line-height:11px;text-transform:uppercase;text-align:center;white-space:nowrap}
  .side__origin b{font-weight:700}
  .side__brand{position:absolute;left:10px;top:488px;width:40px;height:66px;border:2px solid var(--white)}
  .side__brand span{position:absolute;left:10px;top:58px;width:50px;transform-origin:0 0;transform:rotate(-90deg);
    color:var(--white);font-family:"Alfa Slab One",serif;font-size:7px;line-height:16px;white-space:nowrap;text-align:center}
</style>
</head>
<body>

<!-- 52.5 rear -->
<section class="bag bag--premium bag--rear" aria-label="Larkfield cement bag 52.5, rear side">
  <div class="bag__front">
    <div class="rear__brand"><span>LARKFIELD</span></div>
    <p class="rear__title">Applications</p>
    <p class="rear__lead">Suitable for general concrete products.</p>
    <table class="mix-table">
      <tr><th>Cement</th><th>Sand</th><th>Aggregate</th><th>Water</th></tr>
      <tr><td><span class="cup"></span></td><td><span class="cup"></span></td><td><span class="cup"></span></td><td><span class="cup"></span></td></tr>
      <tr><td><span class="cup"></span></td><td><span class="cup"></span></td><td><span class="cup"></span></td><td><span class="cup"></span></td></tr>
    </table>
    <p class="note note--store">Store off the ground</p>
    <p class="note note--use">Keep away from moisture. Keep sealed.</p>
    <div class="rear__grade"><span>Export</span><span>Quality</span><strong>52.5</strong><span>Cement</span></div>
  </div>
  <div class="bag__side">
    <div class="side__icons"><span class="side__dot"></span><span class="side__dot"></span></div>
    <div class="side__grade"><span>Export</span><span>Quality</span><strong>52.5</strong><span>Cement</span></div>
    <div class="side__word">CEMENT</div>
    <div class="side__origin"><b>Export quality</b> product of Myanmar</div>
    <div class="side__brand"><span>LARKFIELD</span></div>
  </div>
</section>

<!-- 52.5 face -->
<section class="bag bag--premium bag--face" aria-label="Larkfield cement bag 52.5, front side">
  <div class="bag__front">
    <div class="bag__rays" role="img" aria-label="Yellow sunburst rays radiating from the lower right"></div>
    <div class="brand-box"><span class="brand-box__name">LARKFIELD</span></div>
    <div class="product-band"><span class="product-band__word">CEMENT</span></div>
    <div class="origin-tag"><b>Export quality</b> product of Myanmar</div>
    <div class="grade-mark"><small>Export</small><small>Quality</small><strong>52.5</strong><small>Cement</small></div>
    <p class="spec">Portland Cement<br>EN 197-1 (2000), Strength Class 42.5</p>
    <div class="usage-icons">
      <span class="usage-icon">KEEP DRY</span>
      <span class="usage-icon">EASY USE</span>
      <span class="usage-icon usage-icon--weight">50kg</span>
    </div>
  </div>
  <div class="bag__side">
    <div class="side__icons"><span class="side__dot"></span><span class="side__dot"></span></div>
    <div class="side__grade"><span>Export</span><span>Quality</span><strong>52.5</strong><span>Cement</span></div>
    <div class="side__word">CEMENT</div>
    <div class="side__origin"><b>Export quality</b> product of Myanmar</div>
    <div class="side__brand"><span>LARKFIELD</span></div>
  </div>
</section>

<!-- 42.5 rear -->
<section class="bag bag--standard bag--rear" aria-label="Larkfield cement bag 42.5, rear side">
  <div class="bag__front">
    <div class="rear__brand"><span>LARKFIELD</span></div>
    <p class="rear__title">Applications</p>
    <p class="rear__lead">Suitable for general concrete products.</p>
    <table class="mix-table">
      <tr><th>Cement</th><th>Sand</th><th>Aggregate</th><th>Water</th></tr>
      <tr><td><span class="cup"></span></td><td><span class="cup"></span></td><td><span class="cup"></span></td><td><span class="cup"></span></td></tr>
      <tr><td><span class="cup"></span></td><td><span class="cup"></span></td><td><span class="cup"></span></td><td><span class="cup"></span></td></tr>
    </table>
    <p class="note note--store">Store off the ground</p>
    <p class="note note--use">Keep away from moisture. Keep sealed.</p>
    <div class="rear__grade"><span>Export</span><span>Quality</span><strong>42.5</strong><span>Cement</span></div>
  </div>
  <div class="bag__side">
    <div class="side__icons"><span class="side__dot"></span><span class="side__dot"></span></div>
    <div class="side__grade"><span>Export</span><span>Quality</span><strong>42.5</strong><span>Cement</span></div>
    <div class="side__word">CEMENT</div>
    <div class="side__origin"><b>Export quality</b> product of Myanmar</div>
    <div class="side__brand"><span>LARKFIELD</span></div>
  </div>
</section>

<!-- 42.5 face -->
<section class="bag bag--standard bag--face" aria-label="Larkfield cement bag 42.5, front side">
  <div class="bag__front">
    <div class="bag__rays" role="img" aria-label="Yellow sunburst rays radiating from the lower right"></div>
    <div class="brand-box"><span class="brand-box__name">LARKFIELD</span></div>
    <div class="product-band"><span class="product-band__word">CEMENT</span></div>
    <div class="origin-tag"><b>Export quality</b> product of Myanmar</div>
    <div class="grade-mark"><small>Export</small><small>Quality</small><strong>42.5</strong><small>Cement</small></div>
    <p class="spec">Portland Cement<br>EN 197-1 (2000), Strength Class 42.5</p>
    <div class="usage-icons">
      <span class="usage-icon">KEEP DRY</span>
      <span class="usage-icon">EASY USE</span>
      <span class="usage-icon usage-icon--weight">50kg</span>
    </div>
  </div>
  <div class="bag__side">
    <div class="side__icons"><span class="side__dot"></span><span class="side__dot"></span></div>
    <div class="side__grade"><span>Export</span><span>Quality</span><strong>42.5</strong><span>Cement</span></div>
    <div class="side__word">CEMENT</div>
    <div class="side__origin"><b>Export quality</b> product of Myanmar</div>
    <div class="side__brand"><span>LARKFIELD</span></div>
  </div>
</section>

</body>
</html>
```